a simple functional website for an up and coming service industry business

hi ,i also require in store promotional items like business cards, flyers, Chatterbox page t-shirts for workers and want all these to have the same look and feel.i need my website to catch the eye .the idea i have in my head is something that will sell the service ,the website is a tool to get people to inquire , book or pay for an assembly service.we assemble flatpack furniture , outdoor furniture,playgrounds etc ,basically anything that comes with instructions,our biggest customer at the moment is Norvalt who we assemble nationally.i am looking for a website to be bright modern and simple to use the current website is www.brindleyfitouts.com which is dull with to many pages . i have already had a new logo designed by sketch harbour and it is lime green and sky blue in colour, a webiste i like is jobtrek q4 although it has lots of flash and my budget probably wouldn't allow that at the moment.

Target Market(s)

customer will be visiting the website to find out about the service we provide , then hopefully making contact,either booking a job or asking for a quote, i like the idea of the phone, email icons on the home screen

Industry/Entity Type

Industry

Requirements
Must have
• a contact icon: when you click on it the page with the name ,email address ,phone number, address pops up

a phone icon : when you click on it the 1300 number pops up
Nice to have
• my current website is with plume and it is www.brindleyfitouts.com

a website i really like the design of is jobtrek q4 and Norvalt

would like some pictures of modern furniture ,bbq's ,gym equipment ,playground equiptment
Should not have
• the career page or price page my current website .i don't want it on there anymore

```html
<!DOCTYPE html>
<html lang="en">
<head>
<meta charset="utf-8">
<title>Kestrel Assembly</title>
<link href="https://fonts.googleapis.com/css2?family=Open+Sans:wght@400;600;700;800&display=swap" rel="stylesheet">
<style>
:root{
  --lime:#8cc63f;
  --lime-dark:#77ad2e;
  --sky:#2a9fd8;
  --ink:#3b3b3b;
  --grey:#7a7a7a;
  --soft:#e6e6e6;
  --bar:#2f2f2f;
  --footer:#3a3a3a;
  --white:#ffffff;
}
*{margin:0;padding:0;box-sizing:border-box}
html,body{width:746px;height:1200px;overflow:hidden;background:var(--white)}
body{font-family:"Open Sans",Arial,sans-serif;color:var(--ink);position:relative}
.abs{position:absolute}

/* header */
.site-header{left:0;top:0;width:746px;height:63px;background:linear-gradient(#ffffff,#eeeeee)}
.brand{left:115px;top:14px;display:flex;align-items:center;gap:8px}
.brand-mark{width:34px;height:34px;background:var(--lime)}
.brand-name{font-size:19px;font-weight:700;line-height:19px;color:var(--lime);letter-spacing:.5px}
.main-nav{left:318px;top:24px;display:flex}
.nav-item{padding:0 10px;border-left:1px solid #d4d4d4;text-align:center}
.nav-item:first-child{border-left:none}
.nav-item .label{display:block;font-size:11px;font-weight:600;color:var(--sky);line-height:13px}
.nav-item .hint{display:block;font-size:8px;color:var(--grey);line-height:12px}
.nav-item.book .label{color:var(--lime);margin-top:0}

/* info bar */
.info-bar{left:0;top:63px;width:746px;height:33px;background:var(--bar)}
.info-bar .green{left:0;top:0;width:316px;height:33px;background:var(--lime);clip-path:polygon(0 0,100% 0,91% 100%,0 100%)}
.phone-line{left:122px;top:66px;display:flex;align-items:center;gap:7px;color:var(--ink);font-size:18px;font-weight:400}
.licence{left:497px;top:68px;font-size:10px;color:var(--white)}

/* hero */
.hero{left:4px;top:96px;width:742px;height:268px;background:linear-gradient(90deg,#5a2e1c 0%,#8a4b2c 20%,#e8e2d4 38%,#3a2317 55%,#c9b98a 75%,#2b1a12 100%)}
.hero-caption{left:408px;top:262px;width:238px;height:48px;background:var(--lime);text-align:center;color:var(--white)}
.hero-caption h1{font-size:19px;font-weight:700;line-height:24px;margin-top:5px}
.hero-caption p{font-size:12px;line-height:14px}
.slider-btn{top:318px;width:31px;height:30px;background:#e4e4e4;display:flex;align-items:center;justify-content:center}

/* what we do */
.intro{left:0;top:380px;width:746px;text-align:center}
.intro h2{font-size:14px;font-weight:700;color:var(--lime)}
.intro p{font-size:10px;color:var(--grey);margin-top:4px}
.intro h3{font-size:15px;font-weight:400;color:var(--ink);margin-top:11px;padding-bottom:8px}
.rule{height:1px;background:linear-gradient(90deg,transparent,#dcdcdc,transparent)}
.service{width:270px}
.service .thumb{position:absolute;left:0;top:0;width:118px;height:76px}
.service .body{position:absolute;left:128px;top:0;width:142px}
.service h4{font-size:11px;font-weight:400;color:var(--ink);line-height:13px}
.service p{font-size:7px;color:var(--grey);line-height:8.6px;margin-top:2px}
.service .more{font-size:7px;font-weight:700;color:var(--lime);margin-top:4px;display:block}
.view-more{left:0;top:675px;width:746px;display:flex;justify-content:center;align-items:center;gap:4px;font-size:13px;color:var(--ink)}

/* quote band */
.quote-band{left:0;top:704px;width:746px;height:248px;background:radial-gradient(circle at 70% 30%,#b7772d 0%,#5a3412 35%,#241309 75%)}
.form-title{left:101px;top:724px;color:var(--white)}
.form-title h2{font-size:14px;font-weight:700;line-height:17px}
.form-title p{font-size:6.5px;font-weight:600;line-height:8px;width:215px}
.field{left:100px;width:230px;height:22px;background:var(--white);font-size:6px;color:#999;padding:7px 0 0 11px}
.field.message{height:75px}
.send{left:100px;top:914px;width:230px;height:25px;background:var(--lime);color:var(--ink);font-size:11px;font-weight:600;text-align:center;line-height:25px}
.quote-copy{left:373px;top:760px;color:var(--white)}
.quote-copy h2{font-size:25px;font-weight:700;line-height:28px}
.quote-copy p{font-size:12px;color:#e8dccb;margin-top:2px}
.call{left:377px;top:843px;color:var(--white)}
.call .now{display:flex;align-items:center;gap:6px;font-size:15px;font-weight:700}
.call .num{font-size:24px;font-weight:700;margin-left:21px;line-height:26px}

/* benefits */
.help-title{left:0;top:968px;width:746px;text-align:center;font-size:15px;color:var(--ink)}
.benefit{width:160px}
.benefit .tick{position:absolute;left:0;top:0}
.benefit h4{position:absolute;left:19px;top:-2px;font-size:10px;font-weight:400;color:var(--sky)}
.benefit p{position:absolute;left:19px;top:12px;width:140px;font-size:6.5px;line-height:8px;color:var(--grey)}

/* footer */
.site-footer{left:0;top:1131px;width:746px;height:69px;background:var(--footer)}
.follow{left:103px;top:1157px;display:flex;align-items:center;gap:8px;color:var(--white);font-size:9px;font-weight:600}
.social{display:flex;gap:5px}
.social span{width:22px;height:22px;border-radius:50%;background:var(--white)}
.footer-links{left:291px;top:1158px;font-size:7px;color:var(--white)}
.footer-links span{padding:0 3px}
.footer-brand{left:488px;top:1148px;display:flex;align-items:center;gap:8px}
.footer-brand .mark{width:34px;height:34px;background:var(--white)}
.footer-brand .name{font-size:17px;font-weight:700;color:var(--white);line-height:18px;letter-spacing:.5px}
.copyright{left:272px;top:1178px;width:202px;height:22px;background:var(--lime);border-radius:6px 6px 0 0;font-size:7px;color:var(--ink);text-align:center;line-height:22px}
</style>
</head>
<body>

<header class="site-header abs"></header>
<div class="brand abs">
  <span class="brand-mark"></span>
  <span class="brand-name">KESTREL<br>ASSEMBLY</span>
</div>
<nav class="main-nav abs">
  <div class="nav-item"><span class="label">ABOUT US</span><span class="hint">Who we are?</span></div>
  <div class="nav-item"><span class="label">SERVICES</span><span class="hint">What we do?</span></div>
  <div class="nav-item"><span class="label">CONTACT US</span><span class="hint">Get in touch</span></div>
  <div class="nav-item book"><span class="label">BOOK &amp; SERVICES</span><span class="hint">&nbsp;</span></div>
</nav>

<div class="info-bar abs"><div class="green abs"></div></div>
<div class="phone-line abs">
  <svg width="18" height="18" viewBox="0 0 24 24"><path fill="#3b3b3b" d="M6.6 10.8a15 15 0 0 0 6.6 6.6l2.2-2.2a1 1 0 0 1 1-.25 11.4 11.4 0 0 0 3.6.57 1 1 0 0 1 1 1V20a1 1 0 0 1-1 1A17 17 0 0 1 3 4a1 1 0 0 1 1-1h3.5a1 1 0 0 1 1 1c0 1.25.2 2.45.57 3.57a1 1 0 0 1-.25 1z"/></svg>
  1300-482-915
</div>
<div class="licence abs">QBSA LICENCE NUMBER:1407265</div>

<section class="hero abs" role="img" aria-label="Photo of a modern bedroom fit out with brick feature wall, TV unit and sliding wardrobe"></section>
<div class="hero-caption abs">
  <h1>DOMESTIC FIT OUTS</h1>
  <p>Domestic Fit Outs Indoor Furniture</p>
</div>
<div class="slider-btn abs" style="left:582px"><svg width="10" height="14" viewBox="0 0 10 14"><path d="M8 1 2 7l6 6" stroke="#333" stroke-width="2.2" fill="none"/></svg></div>
<div class="slider-btn abs" style="left:615px"><svg width="10" height="14" viewBox="0 0 10 14"><path d="m2 1 6 6-6 6" stroke="#333" stroke-width="2.2" fill="none"/></svg></div>

<section class="intro abs">
  <h2>WHAT WE DO?</h2>
  <p>We install DIY flat packed indoor and outdoor living, across South East Queensland for the major retailers.</p>
  <h3>Our Services Include Commercial Fit Out And Domestic Fit Out</h3>
</section>
<div class="rule abs" style="left:150px;top:459px;width:446px"></div>

<article class="service abs" style="left:100px;top:476px">
  <div class="thumb" role="img" aria-label="Photo of an assembled bedroom suite" style="background:linear-gradient(90deg,#6b3a22,#d9cfb8,#3a2418)"></div>
  <div class="body"><h4>Indoor furniture</h4><p>Lorem ipsum dolor sit amet, consectetuer adipiscing elit, sed diam nonummy nibh euismod tincidunt ut laoreet dolore magna aliquam erat volutpat.it, sed diam nonummy nibh euismod tincidunt ut laoreet dolore magna.</p><span class="more">Learn More &gt;&gt;</span></div>
</article>
<article class="service abs" style="left:378px;top:476px">
  <div class="thumb" role="img" aria-label="Photo of outdoor wicker lounge furniture" style="background:linear-gradient(135deg,#cfd6c8,#a38a62,#5e4d36)"></div>
  <div class="body" style="left:130px"><h4>Outdoor Furniture</h4><p>Lorem ipsum dolor sit amet, consectetuer adipiscing elit, sed diam nonummy nibh euismod tincidunt ut laoreet dolore magna aliquam erat volutpat.it, sed diam nonummy nibh euismod tincidunt ut laoreet dolore magna.</p><span class="more">Learn More &gt;&gt;</span></div>
</article>
<article class="service abs" style="left:100px;top:575px">
  <div class="thumb" role="img" aria-label="Photo of a colourful playground with slide" style="background:linear-gradient(180deg,#dbe8f2,#e8b23a 55%,#b83a2a)"></div>
  <div class="body"><h4>Playgrounds</h4><p>Lorem ipsum dolor sit amet, consectetuer adipiscing elit, sed diam nonummy nibh euismod tincidunt ut laoreet dolore magna aliquam erat volutpat.it, sed diam nonummy nibh euismod tincidunt ut laoreet dolore magna.</p><span class="more">Learn More &gt;&gt;</span></div>
</article>
<article class="service abs" style="left:378px;top:575px">
  <div class="thumb" role="img" aria-label="Photo of a row of gym machines" style="background:linear-gradient(180deg,#8d98a6,#2f4fa8 60%,#3a3e48)"></div>
  <div class="body" style="left:130px"><h4>Gyms</h4><p>Lorem ipsum dolor sit amet, consectetuer adipiscing elit, sed diam nonummy nibh euismod tincidunt ut laoreet dolore magna aliquam erat volutpat.it, sed diam nonummy nibh euismod tincidunt ut laoreet dolore magna.</p><span class="more">Learn More &gt;&gt;</span></div>
</article>

<div class="rule abs" style="left:150px;top:666px;width:446px"></div>
<div class="view-more abs">View More Our Services
  <svg width="15" height="15" viewBox="0 0 16 16"><circle cx="8" cy="8" r="8" fill="#8cc63f"/><path d="M6 4.5v7l5.5-3.5z" fill="#fff"/></svg>
</div>

<section class="quote-band abs" role="img" aria-label="Photo of a warmly lit lounge interior with pendant lights and tables"></section>
<div class="form-title abs">
  <h2>FILL OUR CONTACT FORM</h2>
  <p>to discuss your requirements and one of our prompt installers will contact you within 24 business hours.</p>
</div>
<div class="field abs" style="top:762px">NAME</div>
<div class="field abs" style="top:787px">EMAIL</div>
<div class="field abs" style="top:812px">PHONE</div>
<div class="field message abs" style="top:837px">MESSAGE</div>
<div class="send abs">SEND</div>
<div class="quote-copy abs">
  <h2>Get a fixed<br>Price Quote</h2>
  <p>It Only Takes Few Minutes</p>
</div>
<div class="call abs">
  <div class="now"><svg width="16" height="16" viewBox="0 0 24 24"><path fill="#fff" d="M6.6 10.8a15 15 0 0 0 6.6 6.6l2.2-2.2a1 1 0 0 1 1-.25 11.4 11.4 0 0 0 3.6.57 1 1 0 0 1 1 1V20a1 1 0 0 1-1 1A17 17 0 0 1 3 4a1 1 0 0 1 1-1h3.5a1 1 0 0 1 1 1c0 1.25.2 2.45.57 3.57a1 1 0 0 1-.25 1z"/></svg>CALL NOW</div>
  <div class="num">1300-482-915</div>
</div>

<h2 class="help-title abs" style="font-weight:400">How Can We Help Your Assembly Service</h2>

<div class="benefit abs" style="left:109px;top:1014px"><svg class="tick" width="14" height="14" viewBox="0 0 14 14"><circle cx="7" cy="7" r="7" fill="#8cc63f"/><path d="m3.8 7.2 2.2 2.2 4.2-4.4" stroke="#fff" stroke-width="1.8" fill="none"/></svg><h4>Reliability</h4><p>Lorem ipsum dolor sit amet, consectetuer adipiscing elit, sed diam nonummy nibh euismod tincidunt ut laoreet</p></div>
<div class="benefit abs" style="left:283px;top:1014px"><svg class="tick" width="14" height="14" viewBox="0 0 14 14"><circle cx="7" cy="7" r="7" fill="#8cc63f"/><path d="m3.8 7.2 2.2 2.2 4.2-4.4" stroke="#fff" stroke-width="1.8" fill="none"/></svg><h4>Efficiency</h4><p>Lorem ipsum dolor sit amet, consectetuer adipiscing elit, sed diam nonummy nibh euismod tincidunt ut laoreet</p></div>
<div class="benefit abs" style="left:459px;top:1014px"><svg class="tick" width="14" height="14" viewBox="0 0 14 14"><circle cx="7" cy="7" r="7" fill="#8cc63f"/><path d="m3.8 7.2 2.2 2.2 4.2-4.4" stroke="#fff" stroke-width="1.8" fill="none"/></svg><h4>Flexibility</h4><p>Lorem ipsum dolor sit amet, consectetuer adipiscing elit, sed diam nonummy nibh euismod tincidunt ut laoreet</p></div>
<div class="benefit abs" style="left:109px;top:1065px"><svg class="tick" width="14" height="14" viewBox="0 0 14 14"><circle cx="7" cy="7" r="7" fill="#8cc63f"/><path d="m3.8 7.2 2.2 2.2 4.2-4.4" stroke="#fff" stroke-width="1.8" fill="none"/></svg><h4>Excellent Communication</h4><p>Lorem ipsum dolor sit amet, consectetuer adipiscing elit, sed diam nonummy nibh euismod tincidunt ut laoreet</p></div>
<div class="benefit abs" style="left:283px;top:1065px"><svg class="tick" width="14" height="14" viewBox="0 0 14 14"><circle cx="7" cy="7" r="7" fill="#8cc63f"/><path d="m3.8 7.2 2.2 2.2 4.2-4.4" stroke="#fff" stroke-width="1.8" fill="none"/></svg><h4>Personal Shopper/Delivery</h4><p>Lorem ipsum dolor sit amet, consectetuer adipiscing elit, sed diam nonummy nibh euismod tincidunt ut laoreet</p></div>
<div class="benefit abs" style="left:459px;top:1065px"><svg class="tick" width="14" height="14" viewBox="0 0 14 14"><circle cx="7" cy="7" r="7" fill="#8cc63f"/><path d="m3.8 7.2 2.2 2.2 4.2-4.4" stroke="#fff" stroke-width="1.8" fill="none"/></svg><h4>Handyman Services</h4><p>Lorem ipsum dolor sit amet, consectetuer adipiscing elit, sed diam nonummy nibh euismod tincidunt ut laoreet</p></div>

<footer class="site-footer abs"></footer>
<div class="follow abs">FOLLOW US ON
  <div class="social" aria-label="Chirper, Chatterbox, Pinboard"><span title="Chirper"></span><span title="Chatterbox"></span><span title="Pinboard"></span></div>
</div>
<div class="footer-links abs"><span>About Us</span>|<span>Jobs</span>|<span>Privacy</span>|<span>Terms of Use</span>|<span>Sitemap</span></div>
<div class="footer-brand abs"><span class="mark"></span><span class="name">KESTREL<br>ASSEMBLY</span></div>
<div class="copyright abs">© 2013 KESTREL INSTALLATIONS PTY LTD</div>

</body>
</html>
```